Kestrel.vc needs a better website design!

We need a new and better website for Kestrel.vc. We're a Canadian venture capital firm that invests in innovative entrepreneurs. We compete against the following websites: lumora.vc, brightvalefund.ca, osprovc.com, and tessara.vc. We're a diverse group of partners and we're dedicated to the founders we invest in.
Updates

I don’t really like stock photos of random people as part of the website design…so please try to stay away from using those images. Thanks, Owen

Target Market(s)

Canadian entrepreneurs and investors

Industry/Entity Type

Venture capital, finance, investment, entrepreneurship

Coding

Coded - Design and coding required

Number of Pages Required

4 page

Font styles to use
Sans Serif

Colors

Designer to choose colors to be used in the design.

Requirements
Must have
• Clean crisp overall design. Fast and to the point.
Nice to have
• Check out www.kestrel.vc - I did it myself and it is too basic and too wordy.
Should not have
• No stock images with random people in them! Not too wordy or with too many large images that are slow to load.

```html
<!DOCTYPE html>
<html lang="en">
<head>
<meta charset="utf-8">
<title>Kestrel.vc — Venture Capital</title>
<link rel="stylesheet" href="https://fonts.googleapis.com/css2?family=Mulish:wght@400;600;700;800&family=Roboto+Condensed:wght@700&display=swap">
<style>
:root{
  --green:#7a9a2c;
  --green-dark:#5f7d1e;
  --text:#555;
  --heading:#8e8e8e;
  --muted:#9a9a9a;
  --line:#e4e4e4;
  --soft-bg:#f7f7f7;
  --white:#fff;
  --footer-bg:#1c2418;
}
*{box-sizing:border-box;margin:0;padding:0}
html,body{width:1200px;height:2223px;overflow:hidden}
body{position:relative;font-family:"Mulish",sans-serif;color:var(--text);background:var(--white)}

.site-header{position:absolute;top:0;left:0;width:1200px;height:91px;background:var(--white)}
.brand{position:absolute;left:153px;top:22px;display:flex;align-items:center;gap:12px;color:var(--green);font-weight:800;font-size:28px;letter-spacing:.5px}
.brand-dot{width:46px;height:46px;border:3px solid var(--green);border-radius:50%}
.main-nav{position:absolute;right:140px;top:29px;display:flex;align-items:center;gap:33px;font-size:15px}
.main-nav a{color:var(--muted);text-decoration:none}
.main-nav a.is-active{color:var(--green)}
.btn-outline{display:inline-flex;align-items:center;gap:8px;border:1px solid var(--green);color:var(--green)!important;padding:10px 15px;font-size:15px;text-decoration:none}
.main-nav .btn-outline{margin-left:-17px}
.arrow{width:14px;height:8px}

.hero{position:absolute;top:91px;left:0;width:1200px;height:515px}
.hero-photo{position:absolute;inset:0;background:linear-gradient(180deg,#f1d9a6 0%,#e8c88b 22%,#b9b477 42%,#7c9a45 62%,#4e7428 82%,#3b5a1f 100%)}
.hero-title{position:absolute;top:176px;width:100%;text-align:center;font-family:"Roboto Condensed",sans-serif;font-weight:700;font-size:40px;color:var(--white);text-shadow:0 2px 4px rgba(0,0,0,.35)}
.hero-sub{position:absolute;top:235px;left:200px;width:800px;text-align:center;font-weight:600;font-size:26px;line-height:40px;color:var(--white);text-shadow:0 1px 3px rgba(0,0,0,.35)}

.section-title{position:absolute;width:100%;text-align:center;color:var(--heading);font-weight:400;font-size:35px;line-height:45px}
.divider{position:absolute;left:566px;width:80px;height:2px}
.divider::before{content:"";position:absolute;left:0;top:0;width:57px;height:2px;background:var(--green)}
.divider::after{content:"";position:absolute;left:61px;top:0;width:19px;height:2px;background:var(--heading)}

.offer-box{position:absolute;top:809px;left:189px;width:834px;height:131px;border:2px solid #eee}
.offer-text{position:absolute;top:18px;width:300px;font-size:17px;line-height:31px;color:var(--text)}
.offer-text.left{left:18px}
.offer-text.right{left:517px}
.offer-badge{position:absolute;top:789px;left:521px;width:170px;height:170px;border-radius:50%;background:var(--white);border:2px solid #eee;display:flex;align-items:center;justify-content:center}
.offer-badge span{width:120px;height:120px;border:5px solid var(--green);border-radius:50%}

.portfolio{position:absolute;top:1021px;left:0;width:1200px;height:439px;background:var(--soft-bg)}
.portfolio-lead{position:absolute;top:145px;width:100%;text-align:center;font-size:21px;color:var(--muted);margin-left:-20px}
.logo-row{position:absolute;display:flex;gap:15px}
.logo-row.first{top:196px;left:153px}
.logo-row.second{top:295px;left:299px}
.logo-cell{width:139px;height:75px;background:var(--white);border:1px solid #eee;display:flex;align-items:center;justify-content:center;font-weight:700;font-size:19px;color:#8a8a8a}
.logo-cell.is-featured{border:1px solid var(--green)}

.contact-title{top:1513px}
.contact-sub{position:absolute;top:1612px;width:100%;text-align:center;color:var(--green);font-size:17px}
.contact .btn-outline{position:absolute;top:1647px;left:540px;height:41px;padding:0 16px}

.site-footer{position:absolute;top:1781px;left:0;width:1200px;height:442px;overflow:hidden}
.footer-photo{position:absolute;inset:0;background:radial-gradient(ellipse at 30% 60%,#4d7a32 0%,#2c4322 35%,#1c2418 75%,#151a12 100%)}
.footer-content{position:absolute;left:556px;top:0;width:502px;color:var(--white)}
.footer-brand{position:absolute;top:93px;font-weight:800;font-size:28px;letter-spacing:.5px}
.footer-nav{position:absolute;top:148px;display:flex;gap:33px;font-size:16px}
.footer-nav a{color:var(--white);text-decoration:none}
.footer-rule{position:absolute;left:0;width:502px;height:1px;background:rgba(255,255,255,.18)}
.info{position:absolute;top:228px;display:flex;gap:14px;align-items:center}
.info-icon{width:48px;height:48px;border:1px solid var(--green);display:flex;align-items:center;justify-content:center}
.info-label{color:var(--green);font-size:17px}
.info-value{font-size:14px;margin-top:3px}
.copyright{position:absolute;top:332px;font-size:13px;color:#ddd}
.copyright strong{color:var(--white);font-weight:600}
</style>
</head>
<body>

<header class="site-header">
  <div class="brand"><span class="brand-dot"></span>KESTREL.VC</div>
  <nav class="main-nav">
    <a class="is-active" href="#">Home</a>
    <a href="#">What</a>
    <a href="#">How</a>
    <a href="#">Who</a>
    <a class="btn-outline" href="#">Portfolio <svg class="arrow" viewBox="0 0 14 8"><path d="M0 4h12M9 1l3 3-3 3" stroke="currentColor" stroke-width="1.6" fill="none"/></svg></a>
  </nav>
</header>

<section class="hero">
  <div class="hero-photo" role="img" aria-label="Sunrise over rolling green hills"></div>
  <h1 class="hero-title">Kestrel.vc A Venture Capital Firm</h1>
  <p class="hero-sub">We Invest In Innovative Seed Stage Technology Companies In Western Canada Focused On B2B And SaaS Markets</p>
</section>

<section class="offer">
  <h2 class="section-title" style="top:662px">We Are Serial Entrepreneurs And Venture Capital<br>Investors Who Provide</h2>
  <div class="divider" style="top:763px"></div>
  <div class="offer-box">
    <p class="offer-text left">Mentoring and strategic advice to help you grow your company quickly and efficiently</p>
    <p class="offer-text right">Investor introductions to help you raise additional follow-on funding for your startup</p>
  </div>
  <div class="offer-badge"><span></span></div>
</section>

<section class="portfolio">
  <h2 class="section-title" style="top:60px">Our Portfolio</h2>
  <div class="divider" style="top:109px"></div>
  <p class="portfolio-lead">Check Out Our Innovative Portfolio Companies!</p>
  <div class="logo-row first">
    <div class="logo-cell">Coldrun</div>
    <div class="logo-cell">Ledgerly</div>
    <div class="logo-cell">Keyward</div>
    <div class="logo-cell is-featured">Gamera</div>
    <div class="logo-cell">Tillpay</div>
    <div class="logo-cell">Ardent</div>
  </div>
  <div class="logo-row second">
    <div class="logo-cell">Homewise</div>
    <div class="logo-cell">Pulsewell</div>
    <div class="logo-cell">Nutrilab</div>
    <div class="logo-cell">Calmway</div>
  </div>
</section>

<section class="contact">
  <h2 class="section-title contact-title">Contact Us Today If You Have<br>What We’re Looking For</h2>
  <p class="contact-sub">Questions about how we make our venture capital investments?</p>
  <a class="btn-outline" href="#">Contact Us <svg class="arrow" viewBox="0 0 14 8"><path d="M0 4h12M9 1l3 3-3 3" stroke="currentColor" stroke-width="1.6" fill="none"/></svg></a>
</section>

<footer class="site-footer">
  <div class="footer-photo" role="img" aria-label="Young green seedling growing from dark soil"></div>
  <div class="footer-content">
    <div class="footer-brand">KESTREL.VC</div>
    <nav class="footer-nav">
      <a href="#">Home</a><a href="#">What</a><a href="#">How</a><a href="#">Who</a><a href="#">Portfolio</a>
    </nav>
    <div class="footer-rule" style="top:197px"></div>
    <div class="info" style="left:0">
      <div class="info-icon"><svg width="18" height="22" viewBox="0 0 18 22"><path d="M9 21s-7-7.5-7-12a7 7 0 0 1 14 0c0 4.5-7 12-7 12z" fill="none" stroke="#7a9a2c" stroke-width="1.4"/><circle cx="9" cy="9" r="2.5" fill="none" stroke="#7a9a2c" stroke-width="1.4"/></svg></div>
      <div><div class="info-label">Address</div><div class="info-value">Western Canada</div></div>
    </div>
    <div class="info" style="left:246px">
      <div class="info-icon"><svg width="22" height="18" viewBox="0 0 22 18"><rect x="1" y="4" width="20" height="13" fill="none" stroke="#7a9a2c" stroke-width="1.4"/><path d="M1 4l10 7 10-7M4 4V1h14v3" fill="none" stroke="#7a9a2c" stroke-width="1.4"/></svg></div>
      <div><div class="info-label">Email</div><div class="info-value">owen@kestrel.vc</div></div>
    </div>
    <div class="footer-rule" style="top:304px"></div>
    <p class="copyright">Copyright © 2021 <strong>Kestrel Venture Capital</strong>. All Rights Reserved.</p>
  </div>
</footer>

</body>
</html>
```